Pick-n-Plate Gift Coupon

About Us-
Pick-n-Plate is a Tasmanian owned food delivery business which delivers meals from an increasing range of selected restaurants. We provide customers with quality food from reputed restaurants at reasonable delivery charges that meet the highest standards of quality and freshness.
We need some gift coupons/vouchers for our privileged customers. We need three designs which are as follows:
1) 10% OFF
2) FREE DELIVERY
3) FREE DELIVERY when you add any Wine/Beer
Coupons should have following:
Pick-n-Plate Logo
Coupon Code: __________
Note:Redeem this coupon on www.picknplate.com.au

```html
<!DOCTYPE html>
<html lang="en">
<head>
<meta charset="utf-8">
<title>Pick-n-Plate Gift Coupons</title>
<link href="https://fonts.googleapis.com/css2?family=Ubuntu:wght@400;500;700&display=swap" rel="stylesheet">
<style>
  :root {
    --brown: #3b1c0e;
    --orange: #f47920;
    --orange-light: #f9a51f;
    --page: #ececec;
    --white: #ffffff;
  }
  * { margin: 0; padding: 0; box-sizing: border-box; }
  html, body { width: 893px; height: 1200px; overflow: hidden; }
  body {
    background: var(--page);
    font-family: "Ubuntu", sans-serif;
    color: var(--brown);
    position: relative;
  }
  .coupon {
    position: absolute;
    left: 36px;
    width: 817px;
    height: 367px;
    background: var(--white);
    box-shadow: 0 1px 4px rgba(0,0,0,0.35);
    overflow: hidden;
  }
  .coupon--discount { top: 20px; }
  .coupon--delivery { top: 413px; }
  .coupon--drinks { top: 804px; }
  .coupon__band {
    position: absolute; inset: 0; width: 100%; height: 100%;
  }
  .brand__mark {
    position: absolute; left: 21px; top: 21px;
    width: 113px; height: 113px;
    background: var(--orange);
    border-radius: 18px;
  }
  .brand__name {
    position: absolute; left: 154px; top: 27px;
    font-size: 45px; font-weight: 500; line-height: 1;
    color: var(--brown);
  }
  .brand__tagline {
    position: absolute; left: 156px; top: 80px;
    font-size: 25px; font-weight: 400; line-height: 1;
    color: var(--brown);
  }
  .code__label {
    position: absolute; left: 555px; top: 22px; width: 255px;
    text-align: center;
    font-size: 24px; line-height: 1;
    color: var(--brown);
  }
  .code__field {
    position: absolute; left: 555px; top: 56px;
    width: 255px; height: 53px;
    background: var(--white);
    border: 2px solid var(--brown);
    box-shadow: 0 0 0 2px var(--white);
  }
  .coupon__note {
    position: absolute; left: 0; top: 218px; width: 890px;
    text-align: center;
    font-size: 19px; font-weight: 500; line-height: 1;
    color: var(--brown);
  }
  .coupon__note strong { font-weight: 700; }
  .offer {
    position: absolute; left: 0; right: 0;
    text-align: center;
    font-weight: 700; line-height: 1;
    color: var(--brown);
  }
  .offer--discount { top: 262px; font-size: 100px; }
  .offer--delivery { top: 278px; font-size: 72px; }
  .offer--stacked { top: 271px; font-size: 68px; }
  .offer em { font-style: normal; color: var(--orange); }
  .offer__condition {
    position: absolute; left: 0; right: 0; top: 339px;
    text-align: center;
    font-size: 23px; font-weight: 700; line-height: 1;
    color: var(--brown);
  }
</style>
</head>
<body>

<svg width="0" height="0" style="position:absolute" aria-hidden="true">
  <defs>
    <linearGradient id="bandFill" x1="0" y1="0" x2="1" y2="0">
      <stop offset="0" stop-color="#f58a1f"/>
      <stop offset="0.6" stop-color="#f79a1e"/>
      <stop offset="1" stop-color="#f47920"/>
    </linearGradient>
    <g id="band">
      <path d="M0,122 C185,144 392,112 466,0 L613,0 L613,176 C440,168 200,174 0,188 Z" fill="url(#bandFill)"/>
      <path d="M0,106 C180,128 380,98 448,0" fill="none" stroke="#3b1c0e" stroke-width="1.6"/>
      <path d="M0,113 C182,135 386,104 456,0" fill="none" stroke="#f47920" stroke-width="2.4"/>
      <path d="M0,195 C200,181 440,176 613,183" fill="none" stroke="#3b1c0e" stroke-width="1.6"/>
      <path d="M0,202 C200,188 440,183 613,190" fill="none" stroke="#f47920" stroke-width="2.4"/>
    </g>
  </defs>
</svg>

<section class="coupon coupon--discount">
  <svg class="coupon__band" viewBox="0 0 613 275" preserveAspectRatio="none" aria-hidden="true"><use href="#band"/></svg>
  <div class="brand__mark"></div>
  <div class="brand__name">Pick-n-Plate</div>
  <div class="brand__tagline">you pick we deliver</div>
  <div class="code__label">COUPON CODE:</div>
  <div class="code__field"></div>
  <p class="coupon__note">NOTE: REDEEM THIS COUPON ON <strong>www.picknplate.com.au</strong></p>
  <h2 class="offer offer--discount">10 % <em>OFF</em></h2>
</section>

<section class="coupon coupon--delivery">
  <svg class="coupon__band" viewBox="0 0 613 275" preserveAspectRatio="none" aria-hidden="true"><use href="#band"/></svg>
  <div class="brand__mark"></div>
  <div class="brand__name">Pick-n-Plate</div>
  <div class="brand__tagline">you pick we deliver</div>
  <div class="code__label">COUPON CODE:</div>
  <div class="code__field"></div>
  <p class="coupon__note">NOTE: REDEEM THIS COUPON ON <strong>www.picknplate.com.au</strong></p>
  <h2 class="offer offer--delivery">FREE <em>DELIVERY</em></h2>
</section>

<section class="coupon coupon--drinks">
  <svg class="coupon__band" viewBox="0 0 613 275" preserveAspectRatio="none" aria-hidden="true"><use href="#band"/></svg>
  <div class="brand__mark"></div>
  <div class="brand__name">Pick-n-Plate</div>
  <div class="brand__tagline">you pick we deliver</div>
  <div class="code__label">COUPON CODE:</div>
  <div class="code__field"></div>
  <p class="coupon__note">NOTE: REDEEM THIS COUPON ON <strong>www.picknplate.com.au</strong></p>
  <h2 class="offer offer--stacked">FREE <em>DELIVERY</em></h2>
  <p class="offer__condition">WHEN YOU ADD ANY WINE/BEER</p>
</section>

</body>
</html>
```